Sunvale Energy UK Flyer Design, for local domestic and commercial properties.

We are a renewable energy company called "SUNVALE ENERGY UK" we specialize in
Electrical and renewable energy project consultancy.
Solar panel installations
battery storage.
Electrical design and installation from Stage 3

Details can be found on our website: www.sunvaleenergyuk.co.uk
Am looking to have a flyer designed so we can have printed and delivered to all local areas.
We carry out free project surveys and offer full project transparency through out the clients journey.
attached is our logo of which i hope may help.

Target Market(s)

Domestic and commercial properties looking to dramatically reduce energy bills

Industry/Entity Type

Domestic, commercial, industrial, mixed used development and much more.

Font styles to use
Serif
Sans Serif
Decorative

Colors
FFC000
F8CF3A
FAE287
FDF2CF
FEFAEE
F0912C
F2A743
F7CA91
FBE8D2
FDF5EE
EE7325
F08F49
F5BC92
FAE3D3
FDF4ED

Requirements
Must have
• Highlight we offer free quotations and offer a fully transparent project processes from design, installation Plus leading health and safety process no matter what size project.
Nice to have
• Pictures of solar panel systems, i have attached a few pictures which you may wish to edit or take snippets etc.

```html
<!DOCTYPE html>
<html lang="en">
<head>
<meta charset="utf-8">
<title>Sunvale Energy UK – Energy Consulting Flyer</title>
<link href="https://fonts.googleapis.com/css2?family=Montserrat:ital,wght@0,400;0,500;0,600;0,700;0,800;0,900;1,500&display=swap" rel="stylesheet">
<style>
  :root{
    --orange:#EE7325;
    --orange-mid:#F0912C;
    --orange-soft:#F2A743;
    --ink:#2f2f33;
    --grey:#6b6b70;
    --paper:#ffffff;
    --mist:#e9e8e6;
    --photo-roof:#7d8a93;
    --photo-sky:#b9c4cc;
    --photo-brick:#8a6a55;
  }
  *{margin:0;padding:0;box-sizing:border-box}
  html,body{width:900px;height:1200px;overflow:hidden;background:var(--paper)}
  body{font-family:"Montserrat",Arial,sans-serif;color:var(--ink)}
  .flyer{position:relative;width:900px;height:1200px;overflow:hidden;
    background:linear-gradient(180deg,var(--mist) 0%,#f4f3f2 40%,var(--paper) 100%)}

  .brand{position:absolute;left:45px;top:48px;display:flex;align-items:center;gap:10px}
  .brand-dot{width:30px;height:30px;border-radius:50%;background:var(--orange)}
  .brand-name{font-weight:700;font-size:17px;letter-spacing:1px;color:var(--ink)}

  .headline{position:absolute;left:0;right:0;top:148px;text-align:center}
  .headline .kicker{font-weight:600;font-size:27px;letter-spacing:3px;color:var(--ink)}
  .headline .energy{font-weight:800;font-size:138px;line-height:1;color:var(--orange);letter-spacing:2px;margin-top:4px}
  .headline .consulting{font-weight:600;font-size:40px;letter-spacing:12px;color:var(--ink);margin-top:-2px}
  .tagline{font-style:italic;font-weight:500;font-size:17px;color:var(--grey);margin-top:12px;letter-spacing:.5px}
  .tagline .sep{display:inline-block;width:9px;height:9px;background:var(--orange);margin:0 10px 2px}

  .band{position:absolute;left:0;top:0}
  .quote-card{position:absolute;left:75px;top:455px;width:640px;height:130px;
    color:var(--paper);font-size:20px;font-weight:500;line-height:1.45;padding:18px 40px 0 70px}
  .quote-card .mark{position:absolute;font-weight:900;font-size:70px;line-height:1;color:var(--paper)}
  .quote-card .open{left:18px;top:6px}
  .quote-card .close{right:6px;bottom:-28px}

  .photo{position:absolute}
  .photo-roof{left:375px;top:585px;width:525px;height:525px;
    background:linear-gradient(160deg,var(--photo-sky) 0%,var(--photo-roof) 55%,#4f5a61 100%);
    clip-path:polygon(110px 0,100% 0,100% 100%,0 100%,0 110px)}
  .photo-solar{left:0;top:650px;width:490px;height:205px;
    background:linear-gradient(180deg,#9aa7a0 0%,#4c5b63 60%,#303a42 100%)}
  .photo-electrical{left:0;top:870px;width:600px;height:235px;
    background:linear-gradient(135deg,#b7ab9e 0%,var(--photo-brick) 60%,#5a463a 100%);
    clip-path:polygon(0 0,100% 0,520px 100%,0 100%)}

  .service{position:absolute;left:35px;color:var(--paper);font-weight:800;text-transform:uppercase;line-height:1.15}
  .service-solar{top:672px;font-size:34px}
  .service-electrical{top:888px;font-size:34px}

  .cta{position:absolute;left:600px;top:735px;width:300px;height:150px;background:var(--orange);
    color:var(--paper);padding:14px 0 0 22px}
  .cta .get{font-weight:800;font-size:52px;line-height:1}
  .cta .quote{font-weight:800;font-size:62px;line-height:.95}
  .cta .web{font-weight:600;font-size:14px;margin-top:8px}

  .footer{position:absolute;left:0;top:1110px;width:900px;height:90px;background:var(--paper);
    display:flex;align-items:center;padding:0 45px;gap:0}
  .contact{display:flex;align-items:center;gap:12px;font-size:13px;color:var(--grey);line-height:1.35}
  .contact svg{flex:none}
  .contact strong{display:block;font-size:22px;font-weight:700;color:var(--ink)}
  .contact-phone{width:340px}
  .contact-email{width:280px}
</style>
</head>
<body>
<div class="flyer">

  <div class="brand">
    <span class="brand-dot"></span>
    <span class="brand-name">SUNVALE ENERGY UK</span>
  </div>

  <header class="headline">
    <div class="kicker">ELECTRICAL AND RENEWABLE</div>
    <div class="energy">ENERGY</div>
    <div class="consulting">CONSULTING</div>
    <div class="tagline">Free Quotes<span class="sep"></span>Transparent Processes<span class="sep"></span>Leading Health &amp; Safety</div>
  </header>

  <svg class="band" width="900" height="1200" viewBox="0 0 900 1200" aria-hidden="true">
    <polygon points="0,440 860,440 900,400 900,640 0,640" fill="#EE7325"/>
    <polygon points="760,385 900,385 900,420 800,420" fill="#F2A743"/>
    <polyline points="55,470 55,445 120,445" fill="none" stroke="#ffffff" stroke-width="4"/>
    <polyline points="735,575 735,600 670,600" fill="none" stroke="#ffffff" stroke-width="4"/>
  </svg>

  <blockquote class="quote-card">
    <span class="mark open">“</span>
    We offer free quotations and offer a fully transparent project processes from design, installation Plus leading health and safety process no matter what size project.
    <span class="mark close">”</span>
  </blockquote>

  <div class="photo photo-roof" role="img" aria-label="Photo of a house roof with solar panels and an aerial against the sky"></div>
  <div class="photo photo-solar" role="img" aria-label="Photo of a rooftop solar panel array with trees behind"></div>
  <div class="photo photo-electrical" role="img" aria-label="Photo of an inverter and electrical installation on a brick wall"></div>

  <h2 class="service service-solar">Solar Panel<br>Installations</h2>
  <h2 class="service service-electrical">Electrical Design<br>and Installation<br>from Stage 3</h2>

  <div class="cta">
    <div class="get">GET FREE</div>
    <div class="quote">quote</div>
    <div class="web">www.sunvaleenergyuk.co.uk</div>
  </div>

  <footer class="footer">
    <div class="contact contact-phone">
      <svg width="34" height="34" viewBox="0 0 24 24" aria-hidden="true"><path d="M6.6 10.8a15.1 15.1 0 0 0 6.6 6.6l2.2-2.2a1 1 0 0 1 1-.25 11.4 11.4 0 0 0 3.6.57 1 1 0 0 1 1 1V20a1 1 0 0 1-1 1A17 17 0 0 1 3 4a1 1 0 0 1 1-1h3.5a1 1 0 0 1 1 1c0 1.25.2 2.45.57 3.6a1 1 0 0 1-.25 1z" fill="none" stroke="#2f2f33" stroke-width="1.6"/></svg>
      <div>call us for more info<strong>0800 000 4821</strong></div>
    </div>
    <div class="contact contact-email">
      <svg width="30" height="30" viewBox="0 0 24 24" aria-hidden="true"><rect x="2.5" y="5" width="19" height="14" rx="1.5" fill="none" stroke="#2f2f33" stroke-width="1.6"/><path d="M3 6l9 7 9-7" fill="none" stroke="#2f2f33" stroke-width="1.6"/></svg>
      <div>EMAIL<br>info@sunvaleenergyuk.co.uk</div>
    </div>
    <div class="contact contact-address">
      <svg width="30" height="30" viewBox="0 0 24 24" aria-hidden="true"><path d="M12 22s7-7.2 7-12.5A7 7 0 0 0 5 9.5C5 14.8 12 22 12 22z" fill="none" stroke="#2f2f33" stroke-width="1.6"/><circle cx="12" cy="9.5" r="2.5" fill="none" stroke="#2f2f33" stroke-width="1.6"/></svg>
      <div>ADDRESS<br>12 Meadow Row, Ashford, Kent,<br>TN23 9ZZ</div>
    </div>
  </footer>

</div>
</body>
</html>
```